BrivoLane Ute.

I want the full logo on one side. And the other side the card if right Ralf the logo the left half orange like the car in the logo color with Danielle R Morrow
Founder and CEO
Email symbol then dmorrow@brivolaneute.com
Www symbol. Then Brivolaneute.com
Phone symbol then 413-926-BRIV
The very bottom would like Brivo Lane Ute is a division of Harmond Vistas. LLC

```html
<!DOCTYPE html>
<html lang="en">
<head>
<meta charset="utf-8">
<title>Brivo Lane Ute – Business Card</title>
<link rel="stylesheet" href="https://fonts.googleapis.com/css2?family=Open+Sans:wght@400;600;700&display=swap">
<style>
  :root {
    --bg: #e9e9ec;
    --card-white: #ffffff;
    --van-orange: #e8891f;
    --orange-deep: #e07d16;
    --ink: #2f2f33;
    --ink-soft: #4a4a4f;
    --accent-red: #e5242b;
    --stripe-black: #161616;
    --shadow: rgba(0, 0, 0, 0.18);
  }
  * { box-sizing: border-box; margin: 0; padding: 0; }
  html, body { width: 1200px; height: 900px; overflow: hidden; }
  body {
    background: var(--bg);
    font-family: "Open Sans", Arial, sans-serif;
    position: relative;
  }
  .card {
    position: absolute;
    left: 290px;
    width: 620px;
    height: 354px;
    background: var(--card-white);
    box-shadow: 0 6px 18px var(--shadow);
    overflow: hidden;
  }
  .card--contact { top: 66px; }
  .card--logo { top: 480px; }

  .card__art { position: absolute; inset: 0; width: 100%; height: 100%; }

  .brand {
    position: absolute;
    display: flex;
    align-items: center;
    gap: 12px;
    color: var(--ink);
    font-weight: 700;
    letter-spacing: 0.02em;
    white-space: nowrap;
  }
  .brand__dot {
    display: inline-block;
    border-radius: 50%;
    background: var(--van-orange);
  }
  .card--contact .brand { left: 26px; top: 160px; font-size: 22px; }
  .card--contact .brand__dot { width: 24px; height: 24px; }
  .card--logo .brand { left: 50%; top: 50%; transform: translate(-50%, -50%); font-size: 40px; gap: 16px; }
  .card--logo .brand__dot { width: 40px; height: 40px; }

  .accent-rule {
    position: absolute;
    right: 38px;
    top: 26px;
    width: 3px;
    height: 54px;
    background: var(--card-white);
  }
  .contact {
    position: absolute;
    right: 62px;
    top: 40px;
    text-align: right;
    color: var(--ink);
  }
  .contact__name { font-size: 21px; font-weight: 700; color: var(--ink); line-height: 1.2; }
  .contact__role { font-size: 15px; color: var(--ink-soft); margin-bottom: 20px; }
  .contact__list { list-style: none; }
  .contact__item {
    display: flex;
    justify-content: flex-end;
    align-items: center;
    gap: 8px;
    font-size: 14px;
    line-height: 1.25;
    margin-bottom: 4px;
    white-space: nowrap;
  }
  .contact__icon {
    width: 18px; height: 18px;
    border-radius: 50%;
    background: var(--accent-red);
    display: inline-flex; align-items: center; justify-content: center;
    flex: none;
  }
  .contact__icon svg { width: 11px; height: 11px; }
  .division-note {
    position: absolute;
    right: 62px;
    bottom: 34px;
    text-align: right;
    font-size: 14px;
    line-height: 1.3;
    color: var(--ink);
  }
</style>
</head>
<body>

  <section class="card card--contact" aria-label="Business card, contact side">
    <svg class="card__art" viewBox="0 0 620 354" aria-hidden="true">
      <defs>
        <linearGradient id="orangeField" x1="0" y1="0" x2="0" y2="1">
          <stop offset="0" stop-color="#e07d16"/>
          <stop offset="1" stop-color="#e8891f"/>
        </linearGradient>
      </defs>
      <rect width="620" height="354" fill="url(#orangeField)"/>
      <path d="M0 0 H200 C290 40 305 250 245 354 H0 Z" fill="#ffffff"/>
      <path d="M200 0 C290 40 305 250 245 354" fill="none" stroke="#161616" stroke-width="5"/>
      <path d="M213 2 C302 46 317 252 258 354" fill="none" stroke="#e5242b" stroke-width="4"/>
    </svg>

    <div class="brand"><span class="brand__dot"></span>Brivo Lane Ute</div>

    <span class="accent-rule"></span>

    <div class="contact">
      <p class="contact__name">Danielle R Morrow</p>
      <p class="contact__role">Founder and CEO</p>
      <ul class="contact__list">
        <li class="contact__item">413-926-BRIV
          <span class="contact__icon"><svg viewBox="0 0 12 12"><path d="M3 1 L5 3.5 L4 5 C4.6 6.4 5.6 7.4 7 8 L8.5 7 L11 9 L9.8 11 C5.5 10.7 1.3 6.5 1 2.2 Z" fill="#fff"/></svg></span>
        </li>
        <li class="contact__item">dmorrow@brivolaneute.com
          <span class="contact__icon"><svg viewBox="0 0 12 12"><rect x="1" y="2.5" width="10" height="7" fill="#fff"/><path d="M1 2.5 L6 6.5 L11 2.5" fill="none" stroke="#e5242b" stroke-width="1"/></svg></span>
        </li>
        <li class="contact__item">www.Brivolaneute.com
          <span class="contact__icon"><svg viewBox="0 0 12 12"><circle cx="6" cy="6" r="4.6" fill="none" stroke="#fff" stroke-width="1.2"/><ellipse cx="6" cy="6" rx="2" ry="4.6" fill="none" stroke="#fff" stroke-width="1"/><line x1="1.4" y1="6" x2="10.6" y2="6" stroke="#fff" stroke-width="1"/></svg></span>
        </li>
      </ul>
    </div>

    <p class="division-note">Brivo Lane Ute is a division of<br>Harmond Vistas</p>
  </section>

  <section class="card card--logo" aria-label="Business card, logo side">
    <div class="brand"><span class="brand__dot"></span>Brivo Lane Ute</div>
  </section>

</body>
</html>
```